Design some Double Sided Business Cards

***FINAL FILES NEED TO BE SUBMITTED AS LAYERED PSD FILES***

Create a business card for a Home Repair company (logo attached). One side should include logo and contact info (ONLY Name, phone number & email) and the other side should list the services offered (put into 3 columns - 6 services in each column)

For your mockup use this contact info:
Mark Thornbury
555-462-9730
MarkThornbury@[url removed, login to view]

Here are the list of services to add on the back (you can reorder these if need be for spacing reasons):
Flooring
Electric Repairs
Running Wires
Installing Interior/Exterior Lights
Appliance Repairs
Ac Repairs
Painting & Drywall
Counter Tops
Woodwork
Roofing
Plumbing
Tubs & Tile
Demolition
Renovations
Decks
Fences
Window Install & Window Repairs
Custom Interior/Exterior Installs & Designs

```html
<!DOCTYPE html>
<html lang="en">
<head>
<meta charset="utf-8">
<title>Crestline Renovation – Business Cards</title>
<link rel="stylesheet" href="https://fonts.googleapis.com/css2?family=Lato:wght@400;700&display=swap">
<style>
:root{
  --page:#e9e6e1;
  --card:#ffffff;
  --panel:#3d3a3b;
  --maroon:#5b1c1c;
  --ink:#3a3738;
  --teal:#3aa597;
  --light:#f2f2f2;
}
*{box-sizing:border-box;margin:0;padding:0}
html,body{width:1200px;height:821px;overflow:hidden;background:var(--page);font-family:"Lato",Arial,sans-serif}
.canvas{position:relative;width:1200px;height:821px}
.card{position:absolute;width:560px;height:320px;background:var(--card);box-shadow:0 6px 18px rgba(0,0,0,.18)}
.card--back{left:60px;top:60px}
.card--front{left:580px;top:440px}

/* back */
.services-panel{position:absolute;left:24px;top:40px;right:24px;bottom:24px;background:var(--panel);border-radius:12px}
.services-tab{position:absolute;right:34px;top:30px;background:var(--maroon);color:var(--light);font-size:12px;letter-spacing:.5px;padding:4px 14px;border-radius:4px}
.tools-mark{position:absolute;left:50%;top:22px;width:64px;height:50px;margin-left:-32px;background:linear-gradient(135deg,#ffffff,#d9d9d9);border-radius:6px}
.service-columns{position:absolute;left:50px;right:40px;top:100px;display:flex;gap:26px}
.service-list{list-style:none}
.service-list li{display:flex;align-items:center;gap:8px;color:var(--light);font-size:12.5px;line-height:22px;white-space:nowrap}
.service-list:nth-child(2){flex:1}
.bullet{width:12px;height:12px;flex:none}

/* front */
.tools-badge{position:absolute;left:30px;top:40px;width:46px;height:52px;background:linear-gradient(135deg,#3a3738,#3aa597);border-radius:6px}
.person{position:absolute;left:88px;top:44px}
.person__name{font-size:19px;letter-spacing:2px;font-variant:small-caps;color:var(--ink)}
.person__role{font-size:14px;color:var(--maroon);margin-top:2px}
.contact{position:absolute;left:32px;bottom:44px;list-style:none}
.contact li{display:flex;align-items:center;gap:12px;font-size:13px;color:var(--ink);line-height:24px}
.contact svg{width:16px;height:16px;flex:none}
.divider{position:absolute;left:278px;top:40px;width:1px;height:240px;background:var(--maroon)}
.brand{position:absolute;left:300px;right:20px;top:0;bottom:0;display:flex;flex-direction:column;align-items:center;justify-content:center;gap:18px}
.brand__square{width:70px;height:70px;background:var(--maroon)}
.brand__name{font-size:24px;font-weight:700;color:var(--ink);text-align:center;letter-spacing:1px;line-height:1.15}
</style>
</head>
<body>
<main class="canvas">

  <section class="card card--back" aria-label="Card back: services">
    <div class="tools-mark" role="img" aria-label="Crossed wrench and screwdriver illustration"></div>
    <div class="services-panel"></div>
    <div class="services-tab">OUR SERVICES :</div>
    <div class="service-columns">
      <ul class="service-list">
        <li><svg class="bullet" viewBox="0 0 12 12"><circle cx="6" cy="6" r="6" fill="#f2f2f2"/><path d="M5 3.5 7.5 6 5 8.5" stroke="#3d3a3b" stroke-width="1.5" fill="none"/></svg>Flooring</li>
        <li><svg class="bullet" viewBox="0 0 12 12"><circle cx="6" cy="6" r="6" fill="#f2f2f2"/><path d="M5 3.5 7.5 6 5 8.5" stroke="#3d3a3b" stroke-width="1.5" fill="none"/></svg>Roofing</li>
        <li><svg class="bullet" viewBox="0 0 12 12"><circle cx="6" cy="6" r="6" fill="#f2f2f2"/><path d="M5 3.5 7.5 6 5 8.5" stroke="#3d3a3b" stroke-width="1.5" fill="none"/></svg>Plumbing</li>
        <li><svg class="bullet" viewBox="0 0 12 12"><circle cx="6" cy="6" r="6" fill="#f2f2f2"/><path d="M5 3.5 7.5 6 5 8.5" stroke="#3d3a3b" stroke-width="1.5" fill="none"/></svg>Decks</li>
        <li><svg class="bullet" viewBox="0 0 12 12"><circle cx="6" cy="6" r="6" fill="#f2f2f2"/><path d="M5 3.5 7.5 6 5 8.5" stroke="#3d3a3b" stroke-width="1.5" fill="none"/></svg>Fences</li>
      </ul>
      <ul class="service-list">
        <li><svg class="bullet" viewBox="0 0 12 12"><circle cx="6" cy="6" r="6" fill="#f2f2f2"/><path d="M5 3.5 7.5 6 5 8.5" stroke="#3d3a3b" stroke-width="1.5" fill="none"/></svg>Electric Repairs</li>
        <li><svg class="bullet" viewBox="0 0 12 12"><circle cx="6" cy="6" r="6" fill="#f2f2f2"/><path d="M5 3.5 7.5 6 5 8.5" stroke="#3d3a3b" stroke-width="1.5" fill="none"/></svg>AC Repairs</li>
        <li><svg class="bullet" viewBox="0 0 12 12"><circle cx="6" cy="6" r="6" fill="#f2f2f2"/><path d="M5 3.5 7.5 6 5 8.5" stroke="#3d3a3b" stroke-width="1.5" fill="none"/></svg>Running Wires</li>
        <li><svg class="bullet" viewBox="0 0 12 12"><circle cx="6" cy="6" r="6" fill="#f2f2f2"/><path d="M5 3.5 7.5 6 5 8.5" stroke="#3d3a3b" stroke-width="1.5" fill="none"/></svg>Apliance repairs</li>
        <li><svg class="bullet" viewBox="0 0 12 12"><circle cx="6" cy="6" r="6" fill="#f2f2f2"/><path d="M5 3.5 7.5 6 5 8.5" stroke="#3d3a3b" stroke-width="1.5" fill="none"/></svg>Painting and Drywall</li>
        <li><svg class="bullet" viewBox="0 0 12 12"><circle cx="6" cy="6" r="6" fill="#f2f2f2"/><path d="M5 3.5 7.5 6 5 8.5" stroke="#3d3a3b" stroke-width="1.5" fill="none"/></svg>Installing Interior/Exterior Lights</li>
        <li><svg class="bullet" viewBox="0 0 12 12"><circle cx="6" cy="6" r="6" fill="#f2f2f2"/><path d="M5 3.5 7.5 6 5 8.5" stroke="#3d3a3b" stroke-width="1.5" fill="none"/></svg>Window install and Window R.</li>
        <li><svg class="bullet" viewBox="0 0 12 12"><circle cx="6" cy="6" r="6" fill="#f2f2f2"/><path d="M5 3.5 7.5 6 5 8.5" stroke="#3d3a3b" stroke-width="1.5" fill="none"/></svg>Customs Interior/Exterior Inst.</li>
      </ul>
      <ul class="service-list">
        <li><svg class="bullet" viewBox="0 0 12 12"><circle cx="6" cy="6" r="6" fill="#f2f2f2"/><path d="M5 3.5 7.5 6 5 8.5" stroke="#3d3a3b" stroke-width="1.5" fill="none"/></svg>Woodwork</li>
        <li><svg class="bullet" viewBox="0 0 12 12"><circle cx="6" cy="6" r="6" fill="#f2f2f2"/><path d="M5 3.5 7.5 6 5 8.5" stroke="#3d3a3b" stroke-width="1.5" fill="none"/></svg>Tubs and Tiles</li>
        <li><svg class="bullet" viewBox="0 0 12 12"><circle cx="6" cy="6" r="6" fill="#f2f2f2"/><path d="M5 3.5 7.5 6 5 8.5" stroke="#3d3a3b" stroke-width="1.5" fill="none"/></svg>Counter Tops</li>
        <li><svg class="bullet" viewBox="0 0 12 12"><circle cx="6" cy="6" r="6" fill="#f2f2f2"/><path d="M5 3.5 7.5 6 5 8.5" stroke="#3d3a3b" stroke-width="1.5" fill="none"/></svg>Demolition</li>
        <li><svg class="bullet" viewBox="0 0 12 12"><circle cx="6" cy="6" r="6" fill="#f2f2f2"/><path d="M5 3.5 7.5 6 5 8.5" stroke="#3d3a3b" stroke-width="1.5" fill="none"/></svg>Renovations</li>
      </ul>
    </div>
  </section>

  <section class="card card--front" aria-label="Card front: contact">
    <div class="tools-badge" role="img" aria-label="Crossed wrench and screwdriver illustration"></div>
    <div class="person">
      <p class="person__name">Mark Thornbury</p>
      <p class="person__role">Service Manager</p>
    </div>
    <ul class="contact">
      <li><svg viewBox="0 0 16 16"><rect x="4" y="1" width="8" height="14" rx="1.5" fill="none" stroke="#5b1c1c" stroke-width="1.4"/><line x1="7" y1="12.5" x2="9" y2="12.5" stroke="#5b1c1c" stroke-width="1.4"/></svg>555-462-9730</li>
      <li><svg viewBox="0 0 16 16"><rect x="1" y="3" width="14" height="10" fill="#5b1c1c"/><path d="M1 3l7 6 7-6" fill="none" stroke="#ffffff" stroke-width="1.2"/></svg>markthornbury@hearthfix.com</li>
    </ul>
    <div class="divider"></div>
    <div class="brand">
      <div class="brand__square"></div>
      <p class="brand__name">CRESTLINE<br>RENOVATION</p>
    </div>
  </section>

</main>
</body>
</html>
```